Poster Design for Photography Exhibit

We are looking for a poster design for a photography exhibit featuring high-end fashion and celebrity photography.

Name of the exhibit is "MILES DORVAN: UNTITLED" (please use Helvetica Black all cap for show name.

Poster is LANDSCAPE format (2 units wide by 1 unit high).

Unfortunately due to legal reasons, we cannot use any actual Miles Dorvan photos. No can we use fashions or people on the poster!

We are looking for a high-end, sexy, bold provocative design that captures the excitement and glamour of a fashion photo shoot.

Target Market(s)

Men and Women interested in Fashion Photography and art photography in general

Industry/Entity Type

Fashion

Requirements
Must have
• landscape format, name of exhibit in Helvetica Black all caps
Nice to have
• Can be grayscale or color.
Should not have
• Logos or brand names

```html
<!DOCTYPE html>
<html lang="en">
<head>
<meta charset="utf-8">
<title>Miles Dorvan: Untitled — Exhibition Poster</title>
<link rel="stylesheet" href="https://fonts.googleapis.com/css2?family=Inter+Tight:wght@800;900&display=swap">
<style>
  :root {
    --paper: #ffffff;
    --paper-shade: #f1f1f1;
    --void: #000000;
    --void-soft: #1a1a1a;
    --name-white: #ffffff;
    --title-red: #c9040b;
  }
  html, body {
    margin: 0;
    padding: 0;
    width: 1200px;
    height: 848px;
    overflow: hidden;
    background: var(--paper);
  }
  .poster {
    position: relative;
    width: 1200px;
    height: 848px;
    overflow: hidden;
    background: linear-gradient(180deg, var(--paper) 0%, var(--paper-shade) 50%, var(--paper) 100%);
  }
  .torn-opening {
    position: absolute;
    left: 0;
    top: 226px;
    width: 1200px;
    height: 366px;
    background: linear-gradient(180deg,
      var(--paper-shade) 0%,
      var(--void-soft) 6%,
      var(--void) 12%,
      var(--void) 90%,
      var(--void-soft) 95%,
      var(--paper-shade) 100%);
  }
  .poster__type {
    position: absolute;
    inset: 0;
    width: 1200px;
    height: 848px;
    display: block;
  }
  .exhibit-artist {
    font-family: "Inter Tight", "Helvetica Neue", Arial, sans-serif;
    font-weight: 900;
    font-size: 76px;
    fill: var(--name-white);
  }
  .exhibit-title {
    font-family: "Inter Tight", "Helvetica Neue", Arial, sans-serif;
    font-weight: 900;
    font-size: 176px;
    fill: var(--title-red);
  }
</style>
</head>
<body>
<main class="poster">
  <div class="torn-opening" role="img" aria-label="Torn white paper opening onto a black background"></div>
  <svg class="poster__type" viewBox="0 0 1200 848" xmlns="http://www.w3.org/2000/svg">
    <text class="exhibit-artist" x="122" y="378" textLength="958" lengthAdjust="spacing">MILES DORVAN</text>
    <text class="exhibit-title" x="120" y="522" textLength="962" lengthAdjust="spacingAndGlyphs">UNTITLED</text>
  </svg>
</main>
</body>
</html>
```